RKS Rovalin Kestra Sulvane company brochure

We need the design of brochure of a company that provides consultancy, design and supply of key equipment in the field of Wastewater, clean water, organic waste anaerobic treatment and green energy production for Industries. The attached files are:
RKS wording in english that describes activities
Some drawings (useful for design)
Presentation (in italian)
It would be nice to have a 4 pages brochure possibly in double language (english and italian).

Target Market(s)

water and waste

Industry/Entity Type

It Company

Colors

Designer to choose colors to be used in the design.

Requirements
Must have
• use the logo RKS as per attached docs

```html
<!DOCTYPE html>
<html lang="en">
<head>
<meta charset="utf-8">
<title>RKS Rovalin Kestra Sulvane – Company Brochure</title>
<link href="https://fonts.googleapis.com/css2?family=Lato:ital,wght@0,400;0,700;0,900;1,700;1,900&family=Roboto+Condensed:wght@300;400;700&display=swap" rel="stylesheet">
<style>
  :root{
    --canvas:#e3e3e3;
    --paper:#ffffff;
    --ink:#2b2b2b;
    --blue:#1c5f95;
    --blue-photo-a:#2f6f9a;
    --blue-photo-b:#8bb6d2;
    --orange:#e8531b;
    --orange-photo-a:#b3400f;
    --orange-photo-b:#f07a3c;
    --crimson:#d01b4c;
    --green:#3c9a2f;
  }
  *{box-sizing:border-box;margin:0;padding:0}
  html,body{width:1200px;height:1200px;overflow:hidden;background:var(--canvas)}
  body{font-family:"Lato",sans-serif;color:var(--ink);position:relative}

  .spread{position:absolute;left:200px;width:800px;height:566px;display:flex;box-shadow:0 6px 18px rgba(0,0,0,.18)}
  .spread--covers{top:20px}
  .spread--inside{top:614px}
  .page{position:relative;width:400px;height:566px;background:var(--paper);overflow:hidden}

  /* Back cover */
  .back-photo{position:absolute;inset:0;background:linear-gradient(180deg,#bdbdbd 0%,#9a9a9a 35%,#6e6e6e 65%,#3d3d3d 100%)}
  .back-brand{position:absolute;left:40px;bottom:118px;display:flex;align-items:center;gap:10px}
  .brand-dot{width:58px;height:58px;border-radius:50%;background:var(--orange)}
  .back-brand .brand-name{font-weight:900;font-size:30px;color:#fff;letter-spacing:1px}
  .contact{position:absolute;left:40px;bottom:36px;color:#fff;font-family:"Roboto Condensed",sans-serif;font-size:10px;line-height:1.45}
  .contact li{list-style:none;display:flex;align-items:center;gap:7px}
  .contact .strong{font-weight:700;font-size:13px}
  .contact svg{width:10px;height:10px;fill:#fff;flex:none}

  /* Front cover */
  .front-photo{position:absolute;inset:0;background:linear-gradient(180deg,#8b7fd0 0%,#c99ac4 20%,#f1c27a 40%,#f0a14a 48%,#6b6a78 60%,#4b4b52 78%,#2f2f33 100%)}
  .front-brand{position:absolute;top:0;right:22px;width:176px;height:64px;background:#fff;display:flex;align-items:center;justify-content:center}
  .front-brand .brand-name{font-weight:900;font-size:30px;color:var(--green);letter-spacing:1px}
  .front-copy{position:absolute;right:26px;bottom:40px;width:330px;text-align:right;color:#fff}
  .front-copy h1{font-family:"Roboto Condensed",sans-serif;font-weight:700;font-size:19px;line-height:1.1}
  .front-copy h1 span{display:block;font-weight:300}
  .front-copy p{font-size:8.5px;line-height:1.35;margin-top:10px}
  .front-copy .benefits-title{color:var(--orange);font-weight:700;font-size:9.5px;margin-top:8px}
  .front-copy .benefits{margin-top:2px;font-size:9px}

  /* Inside pages */
  .band{position:absolute;left:0;top:0;width:100%}
  .band--blue{height:250px;background:linear-gradient(160deg,#a9c9de 0%,var(--blue-photo-b) 30%,var(--blue-photo-a) 75%,#1d4e74 100%);clip-path:polygon(0 0,100% 0,100% 44%,0 100%)}
  .band--orange{height:200px;background:linear-gradient(160deg,var(--orange-photo-b) 0%,var(--orange) 45%,var(--orange-photo-a) 100%);clip-path:polygon(0 0,100% 0,100% 66%,0 100%)}
  .band-title{position:absolute;color:#fff;font-weight:900;font-size:19px;letter-spacing:.5px}
  .band-title--provide{left:30px;top:214px;transform:rotate(-16deg);transform-origin:left}
  .band-title--tech{left:24px;top:154px;transform:rotate(-8deg);transform-origin:left}

  .drawing{position:absolute;left:0;right:0;bottom:0;background:linear-gradient(180deg,#ffffff 0%,#eeeeee 40%,#d9d9d9 100%)}
  .drawing--left{height:56px}
  .drawing--right{height:160px}

  .page-content{position:absolute;left:34px;right:26px;font-size:9px;line-height:1.3;color:var(--ink);z-index:1}
  .page-content--provide{top:262px}
  .page-content--tech{top:210px;left:30px;font-size:9.5px;line-height:1.35}

  .bullets li{list-style:none;position:relative;padding-left:14px;margin-bottom:2px}
  .bullets li::before{content:"";position:absolute;left:0;top:4px;width:5px;height:5px;background:var(--green)}
  .why-title{color:var(--blue);font-weight:900;font-style:italic;font-size:19px;line-height:1.1;margin:12px 0 7px}

  .tech-list{list-style:none}
  .tech-list > li{margin-bottom:6px}
  .tech-list .num{display:inline-block;width:18px;font-weight:700}
  .tech-list h3{display:inline;color:var(--crimson);font-weight:700;font-size:11.5px}
  .tech-list .sub{list-style:none;padding-left:18px;margin-top:2px}
  .tech-list .sub li{display:flex;gap:8px}
  .tech-list .sub b{font-weight:400;width:10px;flex:none}
</style>
</head>
<body>

<section class="spread spread--covers">
  <article class="page page--back">
    <div class="back-photo" role="img" aria-label="Black and white photo of a steel walkway bridge over a wastewater clarifier at dusk"></div>
    <div class="back-brand">
      <div class="brand-dot"></div>
      <span class="brand-name">RKS</span>
    </div>
    <ul class="contact">
      <li><svg viewBox="0 0 24 24"><path d="M6.6 10.8a15 15 0 0 0 6.6 6.6l2.2-2.2c.3-.3.7-.4 1-.2 1.1.4 2.3.6 3.6.6.6 0 1 .4 1 1V20c0 .6-.4 1-1 1C10.6 21 3 13.4 3 4c0-.6.4-1 1-1h3.5c.6 0 1 .4 1 1 0 1.3.2 2.5.6 3.6.1.3 0 .7-.2 1z"/></svg><span class="strong">011.5820394</span></li>
      <li><svg viewBox="0 0 24 24"><path d="M7 2h10a2 2 0 0 1 2 2v16a2 2 0 0 1-2 2H7a2 2 0 0 1-2-2V4a2 2 0 0 1 2-2zm0 3v13h10V5z"/></svg><span class="strong">347 218 6603</span></li>
      <li><svg viewBox="0 0 24 24"><path d="M12 2a7 7 0 0 0-7 7c0 5 7 13 7 13s7-8 7-13a7 7 0 0 0-7-7zm0 9.5A2.5 2.5 0 1 1 12 6a2.5 2.5 0 0 1 0 5.5z"/></svg><span>RKS SRL - VIA DEI TESSITORI 58/12 - TORINO</span></li>
      <li><svg viewBox="0 0 24 24"></svg><span>PIVA: 10492736058</span></li>
    </ul>
  </article>

  <article class="page page--front">
    <div class="front-photo" role="img" aria-label="Sunset photo of a wastewater treatment basin reflecting a purple and orange sky"></div>
    <div class="front-brand"><span class="brand-name">RKS</span></div>
    <div class="front-copy">
      <h1>RKS VERIFY ANY PROPOSED PROCESS<span>WITH ITS INTERNAL LABS &amp; PILOT TESTS</span></h1>
      <p>RKS Rovalin Kestra Sulvane (RKS) has the mission to solve any client's environmental problem with best process solution available on the market, most reliable and economical both on the CAPEX and OPEX</p>
      <p class="benefits-title">RKS want to optimize the client's benefits :</p>
      <p class="benefits">energy, water recycle, products recovery and emission minimization</p>
    </div>
  </article>
</section>

<section class="spread spread--inside">
  <article class="page page--provide">
    <div class="band band--blue" role="img" aria-label="Blue toned photo of a clarifier bridge and pipe at a treatment plant"></div>
    <h2 class="band-title band-title--provide">WE PROVIDE:</h2>
    <div class="drawing drawing--left" role="img" aria-label="Line drawing of treatment plant buildings and tanks"></div>
    <div class="page-content page-content--provide">
      <ul class="bullets">
        <li>Feasibility studies</li>
        <li>Pilot test</li>
        <li>Process design and guarantees (over 240 plants successfully executed and running)</li>
        <li>Basic and detailed engineering</li>
        <li>Key equipment support</li>
        <li>Construction and start-up supervision</li>
        <li>Operation and supervision expertise (more than 20 years of internal expertise of various biological and chemical reactions)</li>
      </ul>
      <h2 class="why-title">WHY TO CHOOSE US ?</h2>
      <ul class="bullets">
        <li>Cost reduction: RKS first identifies the inefficient processes and remove them.</li>
        <li>Only when the emission reduction is not any more possible or economically feasible, RKS propose the best treatment to the client.</li>
        <li>RKS provide best solutions on a variety of biological and chemical processes</li>
        <li>RKS provide highly qualified and independent consultancy</li>
      </ul>
    </div>
  </article>

  <article class="page page--tech">
    <div class="band band--orange" role="img" aria-label="Orange toned photo of an anaerobic digester dome with railings"></div>
    <h2 class="band-title band-title--tech">PROPOSED TECHNOLOGIES:</h2>
    <div class="drawing drawing--right" role="img" aria-label="Technical line drawing of two anaerobic digestion tanks with labels"></div>
    <div class="page-content page-content--tech">
      <ol class="tech-list">
        <li><span class="num">1.</span><h3>Biological processes:</h3>
          <ol class="sub">
            <li><b>a.</b>Oxidation, nitrification, denitrification, P-removal</li>
            <li><b>b.</b>N-recovery and slow release fertilizers production</li>
            <li><b>c.</b>Anaerobic processes</li>
            <li><b>d.</b>Metal recovery</li>
          </ol>
        </li>
        <li><span class="num">2.</span><h3>High value products recovery</h3></li>
        <li><span class="num">3.</span><h3>Chemico/Phisical processes:</h3>
          <ol class="sub">
            <li><b>a.</b>Flottation</li>
            <li><b>b.</b>Filtration and membrane filtration</li>
            <li><b>c.</b>Chemical oxidations / reductions (e.g. Fenton, colour removal, CN, Cr6+ removal ...)</li>
            <li><b>d.</b>Disinfection</li>
          </ol>
        </li>
      </ol>
    </div>
  </article>
</section>

</body>
</html>
```